Progressive/contemporary business card design for successful Startups as a Service Company

New logo launched in 2020. New website launched in 2021. Now that COVID is (mostly) behind us, I'm networking with more people and need a business card that matches the company/logo design aesthetic.

```html
<!DOCTYPE html>
<html lang="en">
<head>
<meta charset="utf-8">
<title>Launchwise – Business Card</title>
<link rel="stylesheet" href="https://fonts.googleapis.com/css2?family=Lato:wght@400;700;900&display=swap">
<style>
  :root {
    --stage: #1f1f20;
    --card-white: #ffffff;
    --card-dark: #1c1c1d;
    --pattern-a: #222223;
    --pattern-b: #2a2a2a;
    --navy: #3e4b60;
    --ink: #2b2b2b;
    --rule: #8a8a8a;
    --accent-mark: #3e4b60;
  }
  * { box-sizing: border-box; margin: 0; padding: 0; }
  html, body {
    width: 1200px;
    height: 1108px;
    overflow: hidden;
    background: var(--stage);
    font-family: "Lato", Arial, sans-serif;
  }
  .stage {
    position: relative;
    width: 1200px;
    height: 1108px;
  }
  .card {
    position: absolute;
    top: 274px;
    width: 340px;
    height: 560px;
    border-radius: 20px;
    overflow: hidden;
  }
  .card--front {
    left: 215px;
    background: var(--card-white);
    text-align: center;
  }
  .card--back {
    left: 645px;
    background: var(--card-dark);
  }

  /* Front */
  .brand {
    position: absolute;
    top: 126px;
    left: 0;
    right: 0;
    display: flex;
    align-items: center;
    justify-content: center;
    gap: 12px;
  }
  .brand__name {
    font-weight: 400;
    font-size: 30px;
    letter-spacing: 0.2em;
    color: var(--navy);
  }
  .brand__square {
    width: 22px;
    height: 22px;
    background: var(--navy);
  }
  .person {
    position: absolute;
    top: 300px;
    left: 0;
    right: 0;
  }
  .person__name {
    font-weight: 900;
    font-size: 23px;
    letter-spacing: 0.02em;
    text-transform: uppercase;
    color: var(--navy);
    line-height: 1.1;
  }
  .person__title {
    font-size: 17px;
    color: var(--ink);
    margin-top: 2px;
  }
  .icon-row {
    display: flex;
    align-items: center;
    justify-content: center;
    gap: 7px;
    margin: 12px 40px 10px;
  }
  .icon-row__rule {
    flex: 1;
    height: 1px;
    background: var(--rule);
  }
  .icon {
    width: 26px;
    height: 26px;
    border-radius: 4px;
    background: var(--navy);
    display: flex;
    align-items: center;
    justify-content: center;
  }
  .contact {
    font-size: 18px;
    line-height: 1.35;
    color: var(--ink);
  }
  .divider {
    height: 1px;
    background: var(--rule);
    margin: 10px 40px;
  }
  .address {
    font-size: 18px;
    line-height: 1.35;
    color: var(--ink);
  }

  /* Back */
  .back-pattern {
    position: absolute;
    inset: 0;
    background: linear-gradient(135deg, var(--pattern-b) 0%, var(--pattern-a) 55%, var(--card-dark) 100%);
  }
  .back-mark {
    position: absolute;
    right: 72px;
    bottom: 120px;
    width: 30px;
    height: 30px;
    background: var(--accent-mark);
  }
</style>
</head>
<body>
<main class="stage">
  <section class="card card--front" aria-label="Business card front">
    <div class="brand">
      <span class="brand__name">LAUNCHWISE</span>
      <span class="brand__square" aria-hidden="true"></span>
    </div>

    <div class="person">
      <h1 class="person__name">Daniel Hart</h1>
      <p class="person__title">Managing Director</p>

      <div class="icon-row" aria-hidden="true">
        <span class="icon-row__rule"></span>
        <span class="icon">
          <svg width="16" height="16" viewBox="0 0 24 24"><path fill="#fff" d="M6.6 10.8a15.1 15.1 0 0 0 6.6 6.6l2.2-2.2c.3-.3.7-.4 1-.2 1.1.4 2.3.6 3.6.6.6 0 1 .4 1 1V20c0 .6-.4 1-1 1A17 17 0 0 1 3 4c0-.6.4-1 1-1h3.5c.6 0 1 .4 1 1 0 1.3.2 2.5.6 3.6.1.3 0 .7-.2 1z"/></svg>
        </span>
        <span class="icon">
          <svg width="16" height="16" viewBox="0 0 24 24"><rect x="3" y="6" width="18" height="12" fill="none" stroke="#fff" stroke-width="1.8"/><path d="M3 6l9 7 9-7" fill="none" stroke="#fff" stroke-width="1.8"/></svg>
        </span>
        <span class="icon">
          <svg width="16" height="16" viewBox="0 0 24 24"><circle cx="12" cy="12" r="8.5" fill="none" stroke="#fff" stroke-width="1.8"/><path d="M3.5 12h17M12 3.5c3 3 3 14 0 17M12 3.5c-3 3-3 14 0 17" fill="none" stroke="#fff" stroke-width="1.4"/></svg>
        </span>
        <span class="icon-row__rule"></span>
      </div>

      <p class="contact">044-555 010 200<br>hello@launchwise.co<br>www.launchwise.co</p>
      <div class="divider"></div>
      <p class="address">18 Harbour Lane<br>20410, Northland</p>
    </div>
  </section>

  <section class="card card--back" aria-label="Business card back">
    <div class="back-pattern" role="img" aria-label="Dark tonal geometric pattern of interlocking triangles"></div>
    <span class="back-mark" aria-hidden="true"></span>
  </section>
</main>
</body>
</html>
```